Natural Medicine & Health/Fitness Coaching studio requires web page

Require a innovative web page for a studio that coaches clients to better health, nutrition and fitness. The studio compromises of Clinical Nutritionists, Naturopaths, Rehab Trainers, Personal Trainers and Sport Coaches. Would like to see earthy but bold designs emphasizing nutritional health and athletic performance.
Updates

Design only launched today.

Target Market(s)

All genders from 20's to 60's, as well as families

Industry/Entity Type

Nutritionist

Coding

Coded - Design and coding required

Number of Pages Required

3 page

Colors
abd037
3277b5
fbee3d
fece3e
33b8a4
f04a50

Requirements
Must have
• Online booking system, ability to message
• Home page
• Coaching/Fitness page
• Nutritional Medicine page
• Must be suitable for both Fitness and Nutrition

```html
<!DOCTYPE html>
<html lang="en">
<head>
<meta charset="utf-8">
<title>Verdant Form – Nutritional Therapy</title>
<link rel="stylesheet" href="https://fonts.googleapis.com/css2?family=Dancing+Script:wght@500;600&family=Montserrat:wght@400;500;600;700&display=swap">
<style>
:root{
  --green:#9fc63b;
  --blue:#2f74b6;
  --ink:#2b2b2b;
  --text:#5e5e5e;
  --muted:#8a8a8a;
  --line:#d9d9d9;
  --card:#f3f3f3;
  --hero:#e9e9e9;
  --footer:#f4f6f9;
  --white:#ffffff;
}
*{box-sizing:border-box;margin:0;padding:0}
html,body{width:1200px;height:3035px;overflow:hidden}
body{position:relative;background:var(--white);font-family:'Montserrat',sans-serif;color:var(--text)}
.script{font-family:'Dancing Script',cursive;font-weight:600;color:var(--ink)}
.script em{font-style:normal;color:var(--green)}
.btn-outline{position:absolute;display:flex;align-items:center;justify-content:center;border:2px solid var(--green);color:var(--green);font-size:12px;font-weight:600;background:transparent}
.btn-solid{position:absolute;display:flex;align-items:center;justify-content:center;background:var(--green);color:var(--white);font-size:12px;font-weight:600}
.field{position:absolute;border:1px solid var(--line);background:var(--white);font-size:11px;color:#a0a0a0;padding:0 14px;display:flex;align-items:center}

/* header */
.site-header{position:absolute;left:0;top:0;width:1200px;height:96px}
.brand{position:absolute;left:88px;top:18px}
.brand-name{display:flex;align-items:center;gap:8px;font-size:30px;font-weight:700;color:var(--green);line-height:1}
.brand-dot{width:12px;height:12px;border-radius:50%;background:var(--green)}
.brand-tag{font-size:11px;color:var(--blue);margin-top:4px;margin-left:40px;letter-spacing:.5px}
.header-phone{position:absolute;left:740px;top:21px;font-size:17px;font-weight:600;color:var(--ink);display:flex;align-items:center;gap:8px}
.header-phone span{color:var(--green);font-size:14px}
.main-nav{position:absolute;top:64px;left:520px;font-size:12px;font-weight:600}
.main-nav a{position:absolute;white-space:nowrap;text-decoration:none;color:var(--ink)}
.main-nav a.active{color:var(--green)}

/* hero */
.hero{position:absolute;left:0;top:96px;width:1200px;height:480px;background:var(--hero)}
.hero-photo{position:absolute;right:0;top:0;width:700px;height:480px;
  background:
    radial-gradient(ellipse 150px 170px at 66% 32%, rgba(120,80,58,.75), rgba(120,80,58,0) 100%),
    radial-gradient(ellipse 260px 220px at 82% 78%, rgba(38,160,150,.75), rgba(38,160,150,0) 100%),
    radial-gradient(ellipse 190px 120px at 46% 86%, rgba(140,190,90,.7), rgba(140,190,90,0) 100%),
    radial-gradient(ellipse 200px 260px at 70% 20%, rgba(60,40,30,.55), rgba(60,40,30,0) 100%),
    linear-gradient(90deg, #e9e9e9 0%, #e6e4e1 35%, #dedad5 100%);}
.hero-title{position:absolute;left:88px;top:150px;font-size:38px}
.hero-text{position:absolute;left:88px;top:212px;width:490px;font-size:14px;line-height:22px;color:var(--text)}

/* services */
.service-card{position:absolute;top:656px;width:320px;height:360px;background:var(--card)}
.service-photo{width:320px;height:176px}
.service-card h3{position:absolute;left:24px;top:196px;font-size:15px;font-weight:600;color:var(--ink)}
.service-card p{position:absolute;left:24px;top:220px;width:260px;font-size:11.5px;line-height:18px;color:var(--muted)}

/* signup */
.signup{position:absolute;left:0;top:1096px;width:1200px;height:308px;
  background:
    radial-gradient(ellipse 220px 160px at 40% 40%, rgba(60,60,60,.55), rgba(60,60,60,0) 100%),
    radial-gradient(ellipse 240px 140px at 88% 80%, rgba(200,80,50,.55), rgba(200,80,50,0) 100%),
    radial-gradient(ellipse 200px 120px at 70% 90%, rgba(150,170,70,.45), rgba(150,170,70,0) 100%),
    linear-gradient(90deg,#9a9a9a 0%,#c7bfb6 35%,#ddd5cc 60%,#c9bfb2 100%);}
.signup-shade{position:absolute;inset:0;background:rgba(40,40,40,.25)}
.signup h2{position:absolute;left:0;width:1200px;top:54px;text-align:center;font-family:'Dancing Script',cursive;font-weight:600;font-size:34px;color:var(--white)}
.signup p{position:absolute;left:0;width:1200px;top:102px;text-align:center;font-size:14px;color:var(--white)}

/* why */
.why-title{position:absolute;left:0;width:1200px;top:1474px;text-align:center;font-size:34px}
.feature{position:absolute;top:1554px;width:234px;text-align:center}
.feature svg{display:block;margin:0 auto}
.feature h4{margin-top:20px;font-size:15px;font-weight:600;color:var(--ink)}
.feature p{margin-top:10px;font-size:11.5px;line-height:17px;color:var(--muted)}

/* about */
.about{position:absolute;left:0;top:1844px;width:1200px;height:398px}
.about-panel{position:absolute;left:0;top:0;width:600px;height:398px;background:var(--blue)}
.about-photo{position:absolute;left:600px;top:0;width:600px;height:398px;
  background:
    radial-gradient(ellipse 160px 130px at 45% 55%, rgba(238,140,140,.8), rgba(238,140,140,0) 100%),
    radial-gradient(ellipse 120px 180px at 12% 60%, rgba(70,60,55,.6), rgba(70,60,55,0) 100%),
    radial-gradient(ellipse 120px 180px at 88% 55%, rgba(70,60,55,.6), rgba(70,60,55,0) 100%),
    linear-gradient(180deg,#d9cbbd 0%,#c8b7a7 55%,#8c7c70 100%);}
.about h2{position:absolute;left:88px;top:56px;font-family:'Dancing Script',cursive;font-weight:600;font-size:34px;color:var(--white)}
.about .lead{position:absolute;left:88px;top:112px;width:440px;font-size:15px;line-height:22px;color:var(--white)}
.about .body{position:absolute;left:88px;top:176px;width:460px;font-size:12px;line-height:20px;color:#dce8f5}
.btn-light{position:absolute;left:88px;top:296px;width:130px;height:34px;border:2px solid var(--white);color:var(--white);font-size:12px;font-weight:600;display:flex;align-items:center;justify-content:center}

/* message */
.msg-title{position:absolute;left:0;width:1200px;top:2310px;text-align:center;font-size:34px}
.msg-sub{position:absolute;left:0;width:1200px;top:2360px;text-align:center;font-size:14px;color:var(--text)}

/* footer */
.site-footer{position:absolute;left:0;top:2696px;width:1200px;height:339px;background:var(--footer)}
.foot-col{position:absolute;top:80px}
.foot-col h5{font-size:13px;font-weight:600;color:var(--blue);margin-bottom:14px}
.foot-col p,.foot-col li{font-size:12px;line-height:20px;color:var(--text);list-style:none}
.foot-col .foot-call{font-size:22px;color:var(--ink);line-height:28px;margin-bottom:2px}
.socials{display:flex;gap:10px;margin-top:16px}
.socials span{width:22px;height:22px;border-radius:50%;background:#555}
.socials span.on{background:var(--green)}
.badge{position:absolute;left:968px;width:144px}
.foot-rule{position:absolute;left:0;top:266px;width:1200px;height:1px;background:#e0e3e8}
.foot-bottom{position:absolute;top:292px;font-size:11.5px;color:var(--text)}
.to-top{position:absolute;left:1090px;top:288px;width:22px;height:22px;border-radius:50%;background:var(--blue)}
</style>
</head>
<body>

<header class="site-header">
  <div class="brand">
    <div class="brand-name"><span class="brand-dot"></span>Verdant Form</div>
    <div class="brand-tag">Nutritional Therapy</div>
  </div>
  <div class="header-phone"><span>Call:</span>
    <svg width="18" height="18" viewBox="0 0 24 24" fill="none" stroke="#9fc63b" stroke-width="2"><circle cx="12" cy="12" r="10"/><path d="M8.5 7.5c0 4.5 3.5 8 8 8l1-2-2.5-1.2-1 1c-1.5-.7-2.6-1.8-3.3-3.3l1-1L10.5 6.5z" fill="#9fc63b" stroke="none"/></svg>
    (555) 010-2468</div>
  <div class="btn-solid" style="left:936px;top:14px;width:176px;height:32px">Book An Appointment</div>
  <nav class="main-nav">
    <a class="active" style="left:3px">Home</a>
    <a style="left:83px">About Us</a>
    <a style="left:186px">Coaching/Fitness</a>
    <a style="left:340px">Nutritional Medicine</a>
    <a style="left:518px">Contact Us</a>
  </nav>
</header>

<section class="hero">
  <div class="hero-photo" role="img" aria-label="Smiling woman holding a bowl of fresh salad"></div>
  <h1 class="hero-title script">Transform <em>Your Body &amp; Life</em></h1>
  <p class="hero-text">Contrary to popular belief, Lorem Ipsum is not simply random text. It has roots in a piece of classical suffered alteration ...</p>
  <div class="btn-outline" style="left:88px;top:280px;width:128px;height:32px">Explore More</div>
</section>

<section class="services">
  <article class="service-card" style="left:88px">
    <div class="service-photo" role="img" aria-label="Coach guiding a client through a barbell lift" style="background:radial-gradient(ellipse 90px 70px at 35% 45%, rgba(40,110,170,.55), rgba(40,110,170,0) 100%),linear-gradient(180deg,#6b6f78 0%,#4a4e57 60%,#2f3238 100%)"></div>
    <h3>Coaching</h3>
    <p>Lorem Ipsum has been the industry's standard dummy text ever since the 1500s, when an unknown printer took ...</p>
    <div class="btn-outline" style="left:24px;top:300px;width:112px;height:32px">Read More</div>
  </article>
  <article class="service-card" style="left:440px">
    <div class="service-photo" role="img" aria-label="Three women doing lunges in a studio" style="background:radial-gradient(ellipse 140px 60px at 50% 80%, rgba(70,70,75,.45), rgba(70,70,75,0) 100%),linear-gradient(180deg,#c9b9ac 0%,#ddd2c8 50%,#b3a497 100%)"></div>
    <h3>Fitness</h3>
    <p>Lorem Ipsum has been the industry's standard dummy text ever since the 1500s, when an unknown printer took ...</p>
    <div class="btn-outline" style="left:24px;top:300px;width:112px;height:32px">Read More</div>
  </article>
  <article class="service-card" style="left:792px">
    <div class="service-photo" role="img" aria-label="Supplement tubs and bottles on a table" style="background:radial-gradient(ellipse 60px 70px at 68% 45%, rgba(190,80,80,.75), rgba(190,80,80,0) 100%),radial-gradient(ellipse 80px 60px at 40% 60%, rgba(150,150,160,.5), rgba(150,150,160,0) 100%),linear-gradient(180deg,#4a4a52 0%,#3a3a40 60%,#8a8a8a 100%)"></div>
    <h3>Nutritional Medicine</h3>
    <p>Lorem Ipsum has been the industry's standard dummy text ever since the 1500s, when an unknown printer took.</p>
    <div class="btn-solid" style="left:24px;top:300px;width:112px;height:32px">Shop Now!</div>
  </article>
</section>

<section class="signup" role="img" aria-label="Woman working out with dumbbells beside fresh vegetables">
  <div class="signup-shade"></div>
  <h2>Sign-up, Get 10 free Tips</h2>
  <p>Contrary to popular belief, Lorem Ipsum is not simply random</p>
  <div class="field" style="left:284px;top:148px;width:312px;height:32px">Your Name</div>
  <div class="field" style="left:604px;top:148px;width:312px;height:32px">Enter your Email</div>
  <div class="btn-solid" style="left:536px;top:210px;width:128px;height:32px">Sign Up Now!</div>
</section>

<h2 class="why-title script">Why Choose <em>Verdant Form</em></h2>
<div class="feature" style="left:116px">
  <svg width="56" height="56" viewBox="0 0 56 56" fill="none" stroke="#2f74b6" stroke-width="2"><circle cx="28" cy="28" r="22"/><path d="M28 14v14l9 6"/></svg>
  <h4>Open 24 Hours</h4>
  <p>There are many variations of work<br>of Lorem Ipsum available,</p>
</div>
<div class="feature" style="left:350px">
  <svg width="56" height="56" viewBox="0 0 56 56" fill="none" stroke="#2f74b6" stroke-width="2"><path d="M18 24c0-10 20-10 20 0"/><circle cx="28" cy="34" r="15"/><path d="M22 36h12"/></svg>
  <h4>Fitness Training</h4>
  <p>There are many variations of work<br>of Lorem Ipsum available,</p>
</div>
<div class="feature" style="left:583px">
  <svg width="56" height="56" viewBox="0 0 56 56" fill="none" stroke="#2f74b6" stroke-width="2"><circle cx="14" cy="40" r="8"/><circle cx="42" cy="40" r="8"/><path d="M14 40l10-18h12l6 18M24 22l-4-8h-6M36 22l4-8h6"/></svg>
  <h4>Tons of Equipment</h4>
  <p>There are many variations of work<br>of Lorem Ipsum available,</p>
</div>
<div class="feature" style="left:818px">
  <svg width="56" height="56" viewBox="0 0 56 56" fill="none" stroke="#2f74b6" stroke-width="2"><circle cx="18" cy="18" r="6"/><circle cx="38" cy="18" r="6"/><path d="M6 46v-12a6 6 0 0 1 6-6h12a6 6 0 0 1 6 6v12M26 46v-12a6 6 0 0 1 6-6h12a6 6 0 0 1 6 6v12"/></svg>
  <h4>Friendly Staff</h4>
  <p>There are many variations of work<br>of Lorem Ipsum available,</p>
</div>
<div class="btn-outline" style="left:512px;top:1728px;width:176px;height:34px">Book An Appointment</div>

<section class="about">
  <div class="about-panel"></div>
  <div class="about-photo" role="img" aria-label="Group fitness class stretching arms in a gym"></div>
  <h2>About Us</h2>
  <p class="lead">Lorem Ipsum has been the industry's standard dummy text ever since the 1500s, when unknown!</p>
  <p class="body">There are many variations of passages of Lorem Ipsum available, but the majority have suffered alteration in some form, by injected humour, or randomised words which don't look even slightly believable. If you or than are going to use a passage of Lorem Ipsum, you need to be sure there isn't anything embarrassing hidden ...</p>
  <div class="btn-light">Discover More</div>
</section>

<h2 class="msg-title script">Send us <em>Message</em></h2>
<p class="msg-sub">Contrary to popular belief, Lorem Ipsum is not simply random</p>
<div class="field" style="left:204px;top:2416px;width:252px;height:32px">Name</div>
<div class="field" style="left:474px;top:2416px;width:252px;height:32px">Phone</div>
<div class="field" style="left:744px;top:2416px;width:252px;height:32px">Email</div>
<div class="field" style="left:204px;top:2466px;width:792px;height:96px;align-items:flex-start;padding-top:12px">Type your Message here ...</div>
<div class="btn-solid" style="left:536px;top:2584px;width:128px;height:34px">Send Message</div>

<footer class="site-footer">
  <div class="foot-col" style="left:88px">
    <h5>Need Healp? Contact Us</h5>
    <p class="foot-call">Call: (555) 010-2468</p>
    <p>info@verdantform.com</p>
    <div class="socials"><span></span><span class="on"></span><span></span><span></span></div>
  </div>
  <div class="foot-col" style="left:408px">
    <h5>Come Visit Us!</h5>
    <p>4410 Orchard Lane Blvd,<br>Greenvale ML 20415</p>
    <h5 style="margin:14px 0 2px">Trading Hours</h5>
    <p>Mon to Fri: 7.00am to 4.30pm<br>Sat: 8.00am to 11.00am</p>
  </div>
  <div class="foot-col" style="left:728px">
    <h5>Quick Link</h5>
    <ul><li>About Us</li><li>Coaching/Fitness</li><li>Nutritional Medicine</li><li>Contact Us</li></ul>
  </div>
  <div class="badge" style="top:80px;height:62px;background:var(--blue)"></div>
  <div class="badge" style="top:158px;height:54px;background:#222"></div>
  <div class="foot-rule"></div>
  <p class="foot-bottom" style="left:88px">© 2019 Verdant Form. All Right Reserved</p>
  <p class="foot-bottom" style="left:408px">Privacy Policy &nbsp;|&nbsp; Terms and Conditions</p>
  <div class="to-top"></div>
</footer>

</body>
</html>
```